依頼概要
〇依頼の目的/概要
電子書籍(lumora)の表紙デザインをおねがいします。

〇画像サイズ
表紙サイズの理想的な寸法は2560×1600ピクセルです。
注:画像の寸法は1000×625ピクセル以上であることが必要です。
画像の最大の寸法は10000×10000ピクセルです。

〇タイトル
夜更けの庭で青い灯をさがす旅の物語です!

〇帯キャッチ

・眠ることも許されない
死にたくなるようなかゆみと痛みから
柔らかい潤いのある肌になった

・人生の波と家族とのご縁をひもといて
薬を使わずに治す

・「絶対に治る、治ったら
同じように苦しんでいる人の為に役立つ本を書こう」
・・・と決めていました。

デザイナーさんの判断で、
どれかを使ってもらっても、
または全部を使ってもらってもOKです。

〇著者 ぽんたるべカフェ 占導師 千景(柴崎奈緒)

文字の大きさと配置と色のインパクトがあって一目惚れしました。
修正依頼にも迅速な対応もありがたかったです。

初めての電子書籍の執筆と初めてのワークベリーへの仕事依頼で、
ドキドキで、いろいろ小さなわからないところだらけでした。
たくさんの提案、どれも素敵なものばかりですべての提案者の方々に
感謝の氣持ちでいっぱいです。ありがとうございました。
これからもアトピー性皮膚炎を克服するための電子書籍を執筆していく予定なので
また、協力していただけたら嬉しいです。

```html
<!DOCTYPE html>
<html lang="ja">
<head>
<meta charset="utf-8">
<title>夜更けの庭で青い灯をさがす旅の物語です!</title>
<link href="https://fonts.googleapis.com/css2?family=Zen+Maru+Gothic:wght@500;700&display=swap" rel="stylesheet">
<style>
  :root {
    --paper: #ffffff;
    --coral: #ee7753;
    --band: #f7b8a2;
    --ink: #4a3b36;
    --white: #ffffff;
    --art-warm: #fdf1d8;
    --art-soft: #fbe3d6;
  }
  * { margin: 0; padding: 0; box-sizing: border-box; }
  html, body { width: 750px; height: 1200px; overflow: hidden; background: var(--paper); }
  .cover {
    position: relative; width: 750px; height: 1200px; overflow: hidden;
    background: var(--paper);
    font-family: "Zen Maru Gothic", sans-serif;
    color: var(--ink);
  }
  .v { position: absolute; writing-mode: vertical-rl; text-orientation: mixed; white-space: nowrap; }
  .art { position: absolute; border-radius: 12px; }
  .art-woman-top { left: 620px; top: 0; width: 130px; height: 260px;
    background: linear-gradient(160deg, var(--art-soft), var(--art-warm)); }
  .art-mirror-woman { left: 20px; top: 260px; width: 200px; height: 245px;
    background: linear-gradient(200deg, #f1f1f1, var(--art-warm)); }

  .title { color: var(--coral); font-weight: 700; font-size: 62px; line-height: 1; letter-spacing: 0.06em; top: 22px; }
  .title-1 { left: 544px; }
  .title-2 { left: 440px; }
  .title-3 { left: 338px; }

  .author-role { left: 244px; top: 430px; font-size: 19px; font-weight: 500; letter-spacing: 0.08em; }
  .author-name { left: 178px; top: 525px; font-size: 56px; font-weight: 500; letter-spacing: 0.3em; }
  .author-real { left: 244px; top: 660px; font-size: 19px; font-weight: 500; letter-spacing: 0.06em; }

  .band { position: absolute; left: 0; top: 805px; width: 750px; height: 395px; background: var(--band); }

  .small { font-size: 21px; font-weight: 500; line-height: 1.35; letter-spacing: 0.06em; }
  .big { font-size: 34px; font-weight: 700; line-height: 1.3; letter-spacing: 0.06em; }
  .relief-lead { right: 14px; top: 815px; }
  .relief-main { right: 118px; top: 870px; }
  .vow { right: 275px; top: 835px; color: var(--white); font-size: 23px; font-weight: 700; line-height: 1.4; letter-spacing: 0.05em; }
  .method-lead { left: 122px; top: 840px; }
  .method-main { left: 10px; top: 870px; font-size: 38px; }
</style>
</head>
<body>
<main class="cover">
  <div class="art art-woman-top" role="img" aria-label="頬に手を当てて悩む女性のイラスト"></div>
  <div class="art art-mirror-woman" role="img" aria-label="手鏡と、笑顔で肌に触れる女性のイラスト"></div>

  <h1>
    <span class="v title title-1">夜更けの庭で青い</span>
    <span class="v title title-2">灯をさがす旅の</span>
    <span class="v title title-3">物語です!</span>
  </h1>

  <p class="v author-role">ぽんたるべカフェ 占導師</p>
  <p class="v author-name">千景</p>
  <p class="v author-real">(柴崎奈緒)</p>

  <div class="band"></div>

  <p class="v small relief-lead">眠ることも許されない<br>死にたくなるような<br>かゆみと痛みから</p>
  <p class="v big relief-main">柔らかい<br>潤いのある<br>肌になった</p>
  <p class="v vow">「絶対に治る、治ったら<br>同じように苦しんでいる<br>人の為に役立つ本を書こう」<br>…と決めていました。</p>
  <p class="v small method-lead">人生の波と家族との<br>ご縁をひもといて</p>
  <p class="v big method-main">薬を使わずに<br>治す</p>
</main>
</body>
</html>
```